Business Card Design Project

We need a Business Card for an Mechanical Engineering firm in Singapore. The design should be Modern & Technical looking, yet eye catching.

Our company deals in Cutting Tools & Machine Accessories for the Manufacturing Industries such as Oil & Gas, Aero Space, etc... For more information on our Company, you can either email me or view our website www.valtrion.com.sg.

We are trying to revamp our image to give our consumers a fresh new perspective to our company, so we welcome all ideas.

Industry/Entity Type

Business

Requirements
Must have
• Must incorporate New Company Logo into the card as shown in Uploaded file.

```html
<!DOCTYPE html>
<html lang="en">
<head>
<meta charset="utf-8">
<title>Valtrion Tools – Business Card</title>
<link rel="stylesheet" href="https://fonts.googleapis.com/css2?family=Tinos:wght@400;700&display=swap">
<style>
  :root {
    --backdrop: #ececec;
    --card-white: #ffffff;
    --panel-grey: #c6c6c8;
    --accent-red: #e8452c;
    --icon-grey: #8c8c8e;
    --brand-maroon: #7b2242;
    --body-text: #333333;
    --on-red: #ffffff;
  }
  * { box-sizing: border-box; margin: 0; padding: 0; }
  html, body {
    width: 1200px; height: 798px; overflow: hidden;
    background: var(--backdrop);
    font-family: "Tinos", "Times New Roman", serif;
  }
  .canvas { position: relative; width: 1200px; height: 798px; }
  .card {
    position: absolute; left: 75px; top: 99px;
    width: 1050px; height: 600px;
    background: var(--card-white);
    box-shadow: 0 6px 24px rgba(0,0,0,0.12);
    overflow: hidden;
  }
  .card-shapes { position: absolute; inset: 0; }
  .contact-line {
    position: absolute; left: 186px;
    color: var(--on-red); font-size: 24px; line-height: 1;
  }
  .contact-line--phone { top: 229px; }
  .contact-line--fax { top: 275px; }
  .contact-line--email { top: 321px; }
  .address {
    position: absolute; left: 130px; top: 376px;
    color: var(--body-text); font-size: 21px; line-height: 30px;
  }
  .brand-name {
    position: absolute; left: 700px; top: 278px; width: 340px;
    text-align: center;
    color: var(--brand-maroon); font-size: 34px; font-weight: 700;
    letter-spacing: 1px; line-height: 1;
  }
</style>
</head>
<body>
<main class="canvas">
  <section class="card" aria-label="Valtrion Tools business card">
    <svg class="card-shapes" viewBox="0 0 1050 600" width="1050" height="600" aria-hidden="true">
      <!-- grey brand panel and diagonal accent -->
      <polygon points="352,0 1050,0 1050,600 772,600" fill="var(--panel-grey)"/>
      <polygon points="334,0 344,0 764,600 754,600" fill="var(--accent-red)"/>
      <!-- left edge bar -->
      <rect x="40" y="258" width="30" height="200" fill="var(--accent-red)"/>
      <!-- contact bands -->
      <polygon points="172,220 484,220 513,262 172,262" fill="var(--accent-red)"/>
      <polygon points="172,266 516,266 545,308 172,308" fill="var(--accent-red)"/>
      <polygon points="172,312 548,312 577,354 172,354" fill="var(--accent-red)"/>
      <line x1="180" y1="258" x2="468" y2="258" stroke="var(--card-white)" stroke-width="3"/>
      <line x1="180" y1="304" x2="500" y2="304" stroke="var(--card-white)" stroke-width="3"/>
      <!-- icon tiles -->
      <rect x="130" y="220" width="38" height="42" fill="var(--icon-grey)"/>
      <rect x="130" y="266" width="38" height="42" fill="var(--icon-grey)"/>
      <rect x="130" y="312" width="38" height="42" fill="var(--icon-grey)"/>
      <!-- phone icon -->
      <path d="M141 229 l5 -2 l4 8 l-3 3 q3 6 8 9 l3 -3 l8 4 l-2 5 q-12 1 -20 -10 q-6 -8 -3 -14 z" fill="var(--card-white)"/>
      <!-- fax icon -->
      <rect x="140" y="277" width="18" height="9" fill="var(--card-white)"/>
      <rect x="137" y="287" width="24" height="12" fill="var(--card-white)"/>
      <!-- mail icon -->
      <rect x="138" y="323" width="22" height="16" fill="none" stroke="var(--card-white)" stroke-width="2"/>
      <polyline points="138,323 149,333 160,323" fill="none" stroke="var(--card-white)" stroke-width="2"/>
    </svg>

    <p class="contact-line contact-line--phone">65-61234501</p>
    <p class="contact-line contact-line--fax">65-61234502</p>
    <p class="contact-line contact-line--email">hello@valtrion.com.sg</p>

    <address class="address" style="font-style: normal;">
      27 Kallang Way #03-12,<br>
      Kallang Tech Centre, Singapore 349215
    </address>

    <p class="brand-name">VALTRION TOOLS</p>
  </section>
</main>
</body>
</html>
```